Business Card: RW Office Partners - Your tidy answer finder

Business Name: RW Office Partners
Website: www.rwofficepartners.com.au
Email: marisol@rwofficepartners.com.au
Mobile: 61 487 902 346
Facebook: @rwofficepartners
Instrgram: @rwofficepartners

Brading Colours:
HEX
#986474
#ddccd3
#7a8498
#c9d8e4
#000000
#ffffff

Tag Line: Your organised problem solver

Link to DRAFT website:
https://helpdeskhub.sitebuilderx.com/rw-office-partners

About Page from the website:
My name is Marisol Bramwell, and I would love to assist you to become more productive in your day to day and achieve your business and personal goals.
My mission is to give you time, time to work on the important tasks of your business or to be able to spend more time with your family. I will take on the tasks you don’t have time for, don’t know well or simply don’t like to do.
I have an extensive background in Administration, Tender Coordination, Document Control, WHS and Quality Management working primarily in the Construction, Mining and Corporate World.
I am passionate about being organised, having order and making things in your life (and mine) easier! I love to watch something unfold and grow into something amazing! I am known for being the go-to problem solver, the organiser of all things, producing high standards of work even under pressure. I’m also a confident communicator, and I understand that you’re busy running your business.

Target Market(s)

Small to Medium Business who require assistance in their business by a virtual assistant.

Industry/Entity Type

Virtual Assistant

Contact Information for Business Card

Mobile: 61 487 902 346

Font styles to use
Sans Serif

Colors
ffffff

Requirements
Must have
• Branding Colours as outlined.
Contact Details as outlined.
Logo as provided.
Proper contact details - mobile, facebook, instragm, website.
Simple, Elegant, very clean looking.
Should not have
• Note cute with pictures.
Not too girly as still want to market to construction companies.

```html
<!DOCTYPE html>
<html lang="en">
<head>
<meta charset="utf-8">
<title>RW Office Partners – Business Card</title>
<link rel="stylesheet" href="https://fonts.googleapis.com/css2?family=Lato:wght@400&family=Open+Sans:wght@400;600&display=swap">
<style>
  :root {
    --mauve: #986474;
    --slate: #7a8498;
    --ink: #000000;
    --paper: #ffffff;
    --charcoal: #333132;
    --charcoal-soft: #3b393a;
    --front-edge: #e4e4e6;
  }
  * { margin: 0; padding: 0; box-sizing: border-box; }
  html, body {
    width: 1200px; height: 960px; overflow: hidden;
    background: var(--paper);
  }
  .canvas { position: relative; width: 1200px; height: 960px; }

  .card {
    position: absolute;
    overflow: hidden;
    box-shadow: 6px 6px 8px rgba(0,0,0,0.35);
  }
  .card-front {
    left: 246px; top: 39px; width: 720px; height: 426px;
    background: radial-gradient(ellipse at 52% 55%, #ffffff 0%, #f6f6f7 40%, var(--front-edge) 100%);
  }
  .card-back {
    left: 247px; top: 500px; width: 715px; height: 422px;
    background: var(--charcoal);
  }

  .tab { position: absolute; }
  .card-front .tab { top: 148px; width: 36px; height: 130px; background: var(--mauve); }
  .card-front .tab-left { left: 0; border-radius: 0 6px 6px 0; }
  .card-front .tab-right { right: 0; border-radius: 6px 0 0 6px; }
  .card-back .tab { top: 130px; width: 44px; height: 160px; background: var(--paper); }
  .card-back .tab-left { left: 0; border-radius: 0 8px 8px 0; }
  .card-back .tab-right { right: 0; border-radius: 8px 0 0 8px; }

  .brand-name {
    position: absolute;
    font-family: "Open Sans", sans-serif;
    font-weight: 600;
    white-space: nowrap;
  }
  .card-front .brand-name {
    left: 66px; top: 56px;
    font-size: 30px; line-height: 40px;
    color: var(--mauve);
  }
  .card-back .brand-name {
    left: 0; right: 0; top: 150px;
    text-align: center;
    font-size: 40px; line-height: 50px;
    color: var(--paper);
  }

  .headline {
    position: absolute; left: 74px; top: 200px;
    display: flex; align-items: center; gap: 8px;
  }
  .headline svg { width: 26px; height: 30px; }
  .headline-text {
    font-family: "Open Sans", sans-serif;
    font-weight: 400;
    font-size: 23px;
    letter-spacing: 0.2px;
    color: var(--ink);
    white-space: nowrap;
  }

  .contact-list { position: absolute; left: 388px; top: 0; list-style: none; }
  .contact-item {
    position: absolute; left: 0;
    display: flex; align-items: center;
    font-family: "Lato", sans-serif;
    font-size: 15.5px; color: var(--ink);
    white-space: nowrap;
  }
  .contact-item svg { width: 16px; height: 16px; margin-right: 27px; }
  .contact-phone { top: 171px; }
  .contact-web { top: 208px; }
  .contact-mail { top: 251px; }

  .world-map {
    position: absolute; left: 79px; top: 55px; width: 545px; height: 290px;
    background: radial-gradient(ellipse at 50% 50%, var(--charcoal-soft) 0%, var(--charcoal) 75%);
    border-radius: 40px;
  }

  .back-web {
    position: absolute; left: 201px; top: 338px;
    display: flex; align-items: center;
    font-family: "Lato", sans-serif;
    font-size: 17px; color: var(--paper);
    white-space: nowrap;
  }
  .back-web svg { width: 17px; height: 17px; margin-right: 33px; }
</style>
</head>
<body>
<main class="canvas">

  <section class="card card-front" aria-label="Card front">
    <div class="tab tab-left"></div>
    <div class="tab tab-right"></div>

    <p class="brand-name">RW Office Partners</p>

    <div class="headline">
      <svg viewBox="0 0 26 30" aria-hidden="true"><polygon points="0,0 26,15 0,30" fill="#000"/></svg>
      <span class="headline-text">RW OFFICE PARTNERS</span>
    </div>

    <ul class="contact-list">
      <li class="contact-item contact-phone">
        <svg viewBox="0 0 24 24" aria-hidden="true"><path fill="#000" d="M6.6 10.8a15.1 15.1 0 0 0 6.6 6.6l2.2-2.2c.3-.3.7-.4 1-.2 1.1.4 2.3.6 3.6.6.6 0 1 .4 1 1V20c0 .6-.4 1-1 1A17 17 0 0 1 3 4c0-.6.4-1 1-1h3.5c.6 0 1 .4 1 1 0 1.3.2 2.5.6 3.6.1.3 0 .7-.2 1z"/></svg>
        61 487 902 346
      </li>
      <li class="contact-item contact-web">
        <svg viewBox="0 0 24 24" aria-hidden="true"><g fill="none" stroke="#000" stroke-width="1.8"><circle cx="12" cy="12" r="10"/><path d="M3 9h18M3 15h18M12 2c3 3 3 17 0 20M12 2c-3 3-3 17 0 20"/></g></svg>
        www.rwofficepartners.com.au
      </li>
      <li class="contact-item contact-mail">
        <svg viewBox="0 0 24 24" aria-hidden="true"><g fill="none" stroke="#000" stroke-width="2.4"><rect x="2" y="4" width="20" height="16" rx="1"/><path d="M2.5 5.5 12 13l9.5-7.5"/></g></svg>
        marisol@rwofficepartners.com.au
      </li>
    </ul>
  </section>

  <section class="card card-back" aria-label="Card back">
    <div class="world-map" role="img" aria-label="Faint dotted world map background"></div>
    <div class="tab tab-left"></div>
    <div class="tab tab-right"></div>

    <p class="brand-name">RW Office Partners</p>

    <p class="back-web">
      <svg viewBox="0 0 24 24" aria-hidden="true"><g fill="none" stroke="#fff" stroke-width="1.8"><circle cx="12" cy="12" r="10"/><path d="M3 9h18M3 15h18M12 2c3 3 3 17 0 20M12 2c-3 3-3 17 0 20"/></g></svg>
      www.rwofficepartners.com.au
    </p>
  </section>

</main>
</body>
</html>
```